Tolvern Business Cards

Business card design. dont mind if new logo is suggested.
it would be for a security company.
our clients would be bigger security companies around Australia.
have a logo done but can be replaced. see attaached. like the colors.
Need company name, person name, designation, phone and email on front.
At back company logo and name. website saddress and 2 x license numbers
would like to have 2 different background color for both sidde

Industry/Entity Type

Security

Contact Information for Business Card

round corners, front should be light in color. need logo at back with webaddress and 2 x license numners

Font styles to use
Sans Serif

Colors
f37122
faa54b
f8ba93
0255a3
0592cd
85cae6
b3d448
9bcb3c
ffffff

Requirements
Must have
• see description
Nice to have
• see description
Should not have
• should not be difficult to read or hardd to find information on card.. lets say easy on eyes yet catchy

```html
<!DOCTYPE html>
<html lang="en">
<head>
<meta charset="UTF-8">
<title>Tolvern Security Group – Business Cards</title>
<link rel="stylesheet" href="https://fonts.googleapis.com/css2?family=Open+Sans:wght@400;600&display=swap">
<style>
  :root {
    --backdrop: #3a3330;
    --back-card: #111213;
    --back-edge: #1c1d1f;
    --front-card: #f4f6f8;
    --front-edge: #dfe3e7;
    --silver: #b9bbbe;
    --muted-grey: #8e9094;
    --brand-blue: #0255a3;
    --brand-cyan: #0592cd;
    --text-dark: #2a2d31;
  }
  * { margin: 0; padding: 0; box-sizing: border-box; }
  html, body {
    width: 1200px; height: 864px; overflow: hidden;
    background: var(--backdrop);
    font-family: "Open Sans", Arial, sans-serif;
  }
  .canvas { position: relative; width: 1200px; height: 864px; }
  .card {
    position: absolute; width: 560px; height: 320px;
    border-radius: 10px;
    box-shadow: 0 10px 24px rgba(0,0,0,0.45);
    overflow: hidden;
  }
  /* Back of card: dark */
  .card-back { left: 50px; top: 70px; background: var(--back-card); border: 1px solid var(--back-edge); }
  .back-mark {
    position: absolute; left: 50%; top: 70px; transform: translateX(-50%);
    display: flex; align-items: center; gap: 14px;
  }
  .mark-dot { width: 30px; height: 30px; border-radius: 50%; background: var(--silver); }
  .back-name { color: var(--silver); font-size: 26px; font-weight: 600; letter-spacing: 1px; }
  .back-web {
    position: absolute; left: 40px; bottom: 76px;
    color: var(--silver); font-size: 17px; letter-spacing: 6px;
  }
  .back-licence {
    position: absolute; left: 40px; bottom: 46px;
    color: var(--muted-grey); font-size: 14px;
  }
  /* Front of card: light */
  .card-front { left: 590px; top: 474px; background: var(--front-card); border: 1px solid var(--front-edge); }
  .front-brand {
    position: absolute; left: 20px; top: 0; width: 290px; height: 100%;
    display: flex; align-items: center; justify-content: center; gap: 10px;
  }
  .brand-dot { width: 18px; height: 18px; border-radius: 50%; background: var(--brand-cyan); flex: none; }
  .brand-name {
    color: var(--brand-blue); font-size: 17px; font-weight: 600;
    text-transform: uppercase; letter-spacing: 0.5px; white-space: nowrap;
  }
  .divider {
    position: absolute; left: 322px; top: 52px; width: 2px; height: 216px;
    background: linear-gradient(to bottom, rgba(2,85,163,0), rgba(2,85,163,0.7), rgba(2,85,163,0));
  }
  .contact { position: absolute; left: 342px; top: 56px; width: 205px; color: var(--text-dark); }
  .person-name { color: var(--brand-blue); font-size: 17px; font-weight: 600; text-transform: uppercase; line-height: 1.2; }
  .person-role { color: var(--brand-cyan); font-size: 17px; text-transform: uppercase; line-height: 1.3; margin-bottom: 8px; }
  .address { font-size: 14px; line-height: 1.4; margin-bottom: 6px; }
  .contact-list { list-style: none; font-size: 14px; line-height: 1.55; }
  .contact-list li { display: flex; align-items: center; gap: 8px; white-space: nowrap; }
  .contact-list svg { width: 12px; height: 12px; fill: var(--brand-blue); flex: none; }
</style>
</head>
<body>
<main class="canvas">
  <section class="card card-back" aria-label="Card back">
    <div class="back-mark">
      <span class="mark-dot"></span>
      <span class="back-name">Tolvern</span>
    </div>
    <p class="back-web">www.tolvernsecurity.au</p>
    <p class="back-licence">Lic No. #40917236 | #71358204</p>
  </section>

  <section class="card card-front" aria-label="Card front">
    <div class="front-brand">
      <span class="brand-dot"></span>
      <span class="brand-name">Tolvern Security Group</span>
    </div>
    <div class="divider"></div>
    <div class="contact">
      <p class="person-name">Daniel Reeve</p>
      <p class="person-role">CEO/Founder</p>
      <p class="address">412 Harbour Crest Road<br>Fremantle, WA 6160</p>
      <ul class="contact-list">
        <li><svg viewBox="0 0 12 12" aria-hidden="true"><path d="M2.5 1l2 2.2-1 1.3c.6 1.4 1.6 2.4 3 3l1.3-1 2.2 2-1 1.5C5 10 1.9 6.8 1 2z"/></svg>08 9431 7720</li>
        <li><svg viewBox="0 0 12 12" aria-hidden="true"><path d="M1 2.5h10v7H1zM1.6 3l4.4 3.4L10.4 3z" fill-rule="evenodd"/></svg>daniel@tolvernsecurity.au</li>
        <li><svg viewBox="0 0 12 12" aria-hidden="true"><circle cx="6" cy="6" r="5"/></svg>www.tolvernsecurity.au</li>
      </ul>
    </div>
  </section>
</main>
</body>
</html>
```